Government Contracts One Page Marketing Piece

Create a one page flyer. Will need one graphic design created the rest is just layout with the following text

HEADLINE: Introducing Your Newest Customer.

GRAPHIC: (PICTURE OF THE STATE OF IL OR USA WITH IL POPPING OUT.)

UNDER GRAPHIC, SUBHEAD: Thousands of government contracts are awarded to businesses every year. Let's make sure your business is one of them. 

BODY COPY: At 2525, we help you tap into the tremendous amount of government contract work needed for 6,963 units of local government in Illinois. Combining legal, PR, marketing, and lobbying expertise in one stop, we’re ready to be your advocate and connect your business with government.

(SIX BLUE BOXES)

Business Development
2525 keeps a watchful eye out for government opportunities that match up with your business. We do whatever it takes to help you win those contracts. Plus, we have relationships with businesses, unions and nonprofits across the state. We’ll help you win those contracts, too.

Government Marketing
2525 helps you market yourself to government agencies. We refine your message and RFP responses to help you stand out and land the deal.

Procurement Hassles
2525 helps you navigate the procurement process. Procedural errors on RFP, RFI, or RFQ responses can obliterate your chances of winning. We handle the bureaucratic requirements so you can focus on running your business.

Government Relations And Lobbying
2525 is your advocate. Want to change the law or stop a bad piece of legislation? We’ll work with you and policymakers to ensure you are well represented. We also assist in situations where you need government to either help your business or get out of the way.

Strategic Communication
2525 launches PR plans that support your key objectives. Our words and phrases get results, in business and government. We get your message to the right people at the right time. 

Grassroots & Coalition Development
2525 utilizes our experience and relationships to build the largest possible network of supporters to enhance your legislative goals. We build coalitions that bring credibility and emphasize broad-base support.

LOGO, CONTACT

Target Market(s)

businesses that want to grow

Font styles to use
Other font styles liked:
• Trajan Bold

Requirements
Must have
• Image should be of US Map with cities but with a pop out of Illinois with all the cities marked. Would love some cool design for this, would prefer it be one or two colors but not tons. See attached photos that would need to be merged and made to look nice. Illinois would need to be somewhat larger on the pop-out USA image.
• Can you try to variations with different style maps
• Fun style
• http://www.pixelvaultimages.example/pic-455215429/stock-vector-usa-map-word-cloud-collage-with-most-important-cities.html?src=undefined-undefined-21
• and
• http://www.pixelvaultimages.example/pic-103082810/stock-photo-word-cloud-map-of-illinois-state-usa.html?src=PxorPAIOyuLnwqL7O5J1hg-1-7
• Simple style
• http://www.pixelvaultimages.example/pic-251329126/stock-vector-illinois-map.html?src=-P5kt_NviDiYq8QyexsQog-1-6
• and
• http://www.pixelvaultimages.example/pic-34919179/stock-vector-map-of-usa-vector.html?src=ftt8pniMj4Ck2t31iIo1tQ-1-39
Nice to have
• look and feel like my website www.2525counselgroup.example
• font used for logo was Trajan Bold

```html
<!DOCTYPE html>
<html lang="en">
<head>
<meta charset="utf-8">
<title>2525 Counsel Group – Government Contracts Flyer</title>
<link rel="stylesheet" href="https://fonts.googleapis.com/css2?family=Cinzel:wght@400;700&family=Arimo:wght@400&family=Crimson+Pro:wght@400;700&display=swap">
<style>
  :root {
    --navy: #263170;
    --navy-deep: #1f2a66;
    --map-blue: #6d9ccf;
    --map-blue-dark: #4a7fbd;
    --sky: #b9d3e6;
    --tab: #c5d8e8;
    --band-text: #e3e8f6;
    --ink: #1a1a1a;
    --stage: #e7e8ea;
    --paper: #ffffff;
    --footer-link: #d8deef;
  }
  * { box-sizing: border-box; margin: 0; padding: 0; }
  html, body { width: 1200px; height: 1000px; overflow: hidden; }
  body { background: var(--stage); position: relative; font-family: "Arimo", Arial, sans-serif; }

  .flyer {
    position: absolute; left: 276px; top: 42px; width: 648px; height: 916px;
    background: linear-gradient(to bottom, var(--paper) 0%, var(--paper) 70%, #eef0f3 100%);
    overflow: hidden;
  }
  .swoosh { position: absolute; left: 0; top: 0; }

  .brand { position: absolute; left: 36px; top: 26px; display: flex; align-items: center; gap: 10px; }
  .brand-square { width: 62px; height: 62px; background: var(--navy); }
  .brand-name { font-family: "Cinzel", serif; font-weight: 700; font-size: 21px; color: var(--navy); letter-spacing: 0.5px; }

  .map-usa {
    position: absolute; left: 82px; top: 133px; width: 302px; height: 210px;
    background: linear-gradient(160deg, var(--map-blue) 0%, var(--map-blue-dark) 100%);
    border-radius: 30px 60px 40px 70px;
  }
  .map-illinois {
    position: absolute; left: 444px; top: 84px; width: 148px; height: 261px;
    background: linear-gradient(170deg, #5d93cf 0%, var(--map-blue) 100%);
    border-radius: 10px 16px 40px 60px;
  }
  .map-illinois-label {
    position: absolute; left: 454px; top: 182px; width: 130px; text-align: center;
    font-family: "Cinzel", serif; font-weight: 700; font-size: 17px; color: var(--navy);
  }
  .popout-arrow { position: absolute; left: 0; top: 0; }

  .headline {
    position: absolute; left: 0; top: 360px; width: 648px; text-align: center;
    font-family: "Cinzel", serif; font-weight: 700; font-size: 28px; color: var(--navy); letter-spacing: 0.3px;
  }
  .subhead-band {
    position: absolute; left: 0; top: 396px; width: 648px; height: 44px; background: var(--navy);
    display: flex; align-items: center; justify-content: center; text-align: center;
    font-family: "Cinzel", serif; font-size: 14px; line-height: 17px; color: var(--band-text); letter-spacing: 0.4px;
  }
  .intro {
    position: absolute; left: 50px; top: 459px; width: 548px; text-align: center;
    font-size: 12.3px; line-height: 15px; color: var(--ink);
  }

  .services {
    position: absolute; left: 47px; top: 524px; width: 553px;
    display: grid; grid-template-columns: repeat(3, 177px); column-gap: 11px; row-gap: 12px;
  }
  .service { position: relative; height: 144px; background: var(--navy-deep); padding: 29px 9px 0 9px; }
  .service-title {
    position: absolute; left: -2px; right: -2px; top: 6px; height: 17px; background: var(--tab);
    font-family: "Cinzel", serif; font-weight: 700; font-size: 11.5px; color: var(--navy-deep);
    display: flex; align-items: center; justify-content: center; white-space: nowrap;
  }
  .service-title.is-long { font-size: 8.6px; }
  .service-text { font-size: 10.4px; line-height: 12.2px; color: #f2f4fa; text-align: justify; }

  .footer { position: absolute; left: 0; top: 848px; }
  .footer-address {
    position: absolute; left: 36px; top: 862px; white-space: nowrap;
    font-family: "Crimson Pro", Georgia, serif; font-weight: 700; font-size: 16px; color: #ffffff;
  }
  .footer-links {
    position: absolute; left: 36px; top: 886px; display: flex; gap: 16px; white-space: nowrap;
    font-family: "Crimson Pro", Georgia, serif; font-size: 12px; color: var(--footer-link);
  }
  .footer-links span { display: inline-flex; align-items: center; gap: 4px; }
  .footer-phone {
    position: absolute; right: 46px; top: 873px; display: flex; align-items: center; gap: 6px; white-space: nowrap;
    font-family: "Crimson Pro", Georgia, serif; font-weight: 700; font-size: 25px; color: #ffffff;
  }
</style>
</head>
<body>
  <main class="flyer">
    <svg class="swoosh" width="648" height="300" viewBox="0 0 648 300" aria-hidden="true">
      <defs>
        <linearGradient id="swooshFill" x1="0" y1="0" x2="1" y2="0">
          <stop offset="0" stop-color="#a9c8e0"/>
          <stop offset="0.6" stop-color="#d6e6f1"/>
          <stop offset="1" stop-color="#ffffff" stop-opacity="0"/>
        </linearGradient>
      </defs>
      <path d="M0 0 H648 V40 C470 50 260 95 0 215 Z" fill="url(#swooshFill)"/>
    </svg>

    <div class="brand">
      <div class="brand-square"></div>
      <div class="brand-name">2525 Counsel Group</div>
    </div>

    <div class="map-usa" role="img" aria-label="Map of the United States in light blue with state outlines, Illinois highlighted in a darker blue"></div>
    <div class="map-illinois" role="img" aria-label="Enlarged map of Illinois in blue showing its county outlines"></div>
    <div class="map-illinois-label">Illinois</div>

    <svg class="popout-arrow" width="648" height="300" viewBox="0 0 648 300" aria-hidden="true">
      <path d="M318 205 C335 160 380 140 440 150" fill="none" stroke="#1f3d8a" stroke-width="9" stroke-linecap="round"/>
      <path d="M432 134 L458 152 L430 166 Z" fill="#1f3d8a"/>
    </svg>

    <h1 class="headline">Introducing Your Newest Customer</h1>
    <p class="subhead-band">Thousands of government contracts are awarded to businesses<br>every year. Let’s make sure your business is one of them.</p>

    <p class="intro">At 2525, we help you tap into the tremendous amount of government contract work needed for 6,963 units of local government in Illinois. Combining legal, PR, marketing, and lobbying expertise in one stop, we’re ready to be your advocate and connect your business with government.</p>

    <section class="services">
      <article class="service">
        <h2 class="service-title">Business Development</h2>
        <p class="service-text">2525 keeps a watchful eye out for government opportunities that match up with your business. We do whatever it takes to help you win those contracts. Plus, we have relationships with businesses, unions and nonprofits across the state. We’ll help you win those contracts, too.</p>
      </article>
      <article class="service">
        <h2 class="service-title">Government Marketing</h2>
        <p class="service-text">2525 helps you market yourself to government agencies. We refine your message and RFP responses to help you stand out and land the deal.</p>
      </article>
      <article class="service">
        <h2 class="service-title">Procurement Hassles</h2>
        <p class="service-text">2525 helps you navigate the procurement process. Procedural errors on RFP, RFI, or RFQ responses can obliterate your chances of winning. We handle the bureaucratic requirements so you can focus on running your business.</p>
      </article>
      <article class="service">
        <h2 class="service-title is-long">Government Relations And Lobbying</h2>
        <p class="service-text">2525 is your advocate. Want to change the law or stop a bad piece of legislation? We’ll work with you and policymakers to ensure you are well represented. We also assist in situations where you need government to either help your business or get out of the way.</p>
      </article>
      <article class="service">
        <h2 class="service-title">Strategic Communication</h2>
        <p class="service-text">2525 launches PR plans that support your key objectives. Our words and phrases get results, in business and government. We get your message to the right people at the right time.</p>
      </article>
      <article class="service">
        <h2 class="service-title is-long">Grassroots &amp; Coalition Development</h2>
        <p class="service-text">2525 utilizes our experience and relationships to build the largest possible network of supporters to enhance your legislative goals. We build coalitions that bring credibility and emphasize broad-base support.</p>
      </article>
    </section>

    <svg class="footer" width="648" height="68" viewBox="0 0 648 68" aria-hidden="true">
      <path d="M0 0 H372 L386 22 H648 V68 H0 Z" fill="var(--navy)"/>
      <path d="M372 0 L386 22 H648" fill="none" stroke="#8fb2d6" stroke-width="2"/>
    </svg>
    <p class="footer-address">48 W Harlow St, 12th Floor, Chicago, IL 60610</p>
    <p class="footer-links">
      <span><svg width="10" height="8" viewBox="0 0 10 8" aria-hidden="true"><rect x="0.5" y="0.5" width="9" height="7" fill="none" stroke="#d8deef"/><path d="M0.5 0.5 L5 4.5 L9.5 0.5" fill="none" stroke="#d8deef"/></svg>casey@2525counselgroup.example</span>
      <span><svg width="9" height="9" viewBox="0 0 10 10" aria-hidden="true"><circle cx="5" cy="5" r="4.5" fill="none" stroke="#d8deef"/><path d="M0.5 5 H9.5 M5 0.5 C2 3 2 7 5 9.5 M5 0.5 C8 3 8 7 5 9.5" fill="none" stroke="#d8deef"/></svg>www.2525counselgroup.example</span>
    </p>
    <p class="footer-phone">
      <svg width="18" height="18" viewBox="0 0 20 20" aria-hidden="true"><circle cx="10" cy="10" r="9" fill="none" stroke="#ffffff" stroke-width="1.5"/><path d="M7 5 L9 7.5 L8 9 C8.8 10.6 9.6 11.4 11 12 L12.5 11 L15 13 L13.5 15 C9.5 14.5 5.5 10.5 5 6.5 Z" fill="#ffffff"/></svg>
      312-555-0148
    </p>
  </main>
</body>
</html>
```